Torvane Aviation Limited

Started a consulting business 12 months ago and have since moved location and have grown and seek to identify my self to the industry.
Specializing in quality solutions, business documentation and maintenance solution's

Industry/Entity Type

Business

```html
<!DOCTYPE html>
<html lang="en">
<head>
<meta charset="utf-8">
<title>Torvane Aviation Limited – Business Card</title>
<link rel="stylesheet" href="https://fonts.googleapis.com/css2?family=Poiret+One&family=Josefin+Sans:wght@400&display=swap">
<style>
  :root {
    --backdrop: #2a2a2a;
    --card-black: #161616;
    --card-black-light: #262626;
    --card-grey-light: #f2f2f2;
    --card-grey-dark: #9a9a9a;
    --accent: #f26a21;
    --accent-soft: #e0732f;
    --text-light: #e8e8e8;
    --text-dark: #2b2b2b;
    --divider: #3a3a3a;
    --mark-fill: #1c1c1c;
  }
  * { box-sizing: border-box; margin: 0; padding: 0; }
  html, body {
    width: 1200px; height: 1134px; overflow: hidden;
    background: var(--backdrop);
  }
  .canvas {
    position: relative; width: 1200px; height: 1134px;
    font-family: "Poiret One", sans-serif;
  }

  .card {
    position: absolute; width: 540px; height: 310px;
    border-radius: 2px; overflow: hidden;
    box-shadow: 0 18px 40px rgba(0,0,0,.55);
  }
  .card--front {
    left: 40px; top: 150px;
    background: radial-gradient(circle at 45% 40%, var(--card-black-light), var(--card-black) 70%);
  }
  .card--back {
    left: 620px; top: 150px;
    background: radial-gradient(circle at 55% 40%, var(--card-grey-light), var(--card-grey-dark) 95%);
  }

  .brand {
    position: absolute; display: flex; flex-direction: column; align-items: center;
  }
  .brand__disc {
    border-radius: 50%; background: var(--mark-fill);
  }
  .brand__name {
    font-family: "Poiret One", sans-serif; letter-spacing: 2px; white-space: nowrap;
  }

  .card--front .brand { left: 30px; top: 70px; width: 220px; }
  .card--front .brand__disc { width: 96px; height: 96px; background: #3b3b3b; }
  .card--front .brand__name { margin-top: 22px; font-size: 17px; color: var(--text-light); }

  .card__divider {
    position: absolute; left: 270px; top: 40px; width: 1px; height: 200px;
    background: var(--divider);
  }

  .contact { position: absolute; left: 295px; top: 62px; width: 230px; }
  .contact__name { font-size: 30px; color: var(--accent); letter-spacing: 2px; }
  .contact__title {
    font-family: "Josefin Sans", sans-serif; font-size: 17px; color: var(--text-light);
    letter-spacing: 1.5px; margin-top: 2px;
  }
  .contact__list { list-style: none; margin-top: 28px; }
  .contact__item {
    display: flex; align-items: flex-start; gap: 10px;
    font-size: 11.5px; line-height: 15px; color: var(--accent-soft); margin-bottom: 8px;
  }
  .contact__icon { width: 13px; height: 13px; flex: none; margin-top: 1px; }

  .card__stripe {
    position: absolute; left: 0; right: 0; bottom: 26px; height: 9px;
    background: var(--accent);
  }

  .card--back .brand { left: 0; right: 0; top: 40px; }
  .card--back .brand__disc {
    width: 150px; height: 150px;
    box-shadow: 0 0 0 10px #6a6a6a;
  }
  .card--back .brand__name { margin-top: 36px; font-size: 30px; color: var(--text-dark); }

  .lockup {
    position: absolute; left: 0; right: 0; top: 620px;
    display: flex; flex-direction: column; align-items: center;
  }
  .lockup .brand__disc {
    width: 170px; height: 170px; background: var(--mark-fill);
    box-shadow: 0 0 0 12px #7a7a7a;
  }
  .lockup .brand__name { margin-top: 50px; font-size: 46px; color: var(--text-light); letter-spacing: 4px; }
</style>
</head>
<body>
<main class="canvas">

  <section class="card card--front" aria-label="Business card front">
    <div class="brand">
      <div class="brand__disc"></div>
      <p class="brand__name">Torvane Aviation Limited</p>
    </div>
    <div class="card__divider"></div>
    <div class="contact">
      <h1 class="contact__name">Marcus D Hale</h1>
      <p class="contact__title">Job title</p>
      <ul class="contact__list">
        <li class="contact__item">
          <svg class="contact__icon" viewBox="0 0 12 12"><path d="M6 0.5a3.6 3.6 0 0 0-3.6 3.6C2.4 7 6 11.5 6 11.5S9.6 7 9.6 4.1A3.6 3.6 0 0 0 6 0.5z" fill="#d9d9d9"/><circle cx="6" cy="4.1" r="1.3" fill="#161616"/></svg>
          <span>Unit 4B, 18 Kereru Lane<br>Penrose 1061, Auckland NZ</span>
        </li>
        <li class="contact__item">
          <svg class="contact__icon" viewBox="0 0 12 12"><path d="M1 4.2C1 2.5 3 1.5 6 1.5s5 1 5 2.7l-2 .6-.4-1.4H3.4L3 4.8z" fill="#d9d9d9"/><rect x="2.5" y="5.5" width="7" height="5" rx="1" fill="#d9d9d9"/></svg>
          <span>+64 21 555 0148</span>
        </li>
        <li class="contact__item">
          <svg class="contact__icon" viewBox="0 0 12 12"><rect x="0.5" y="2.5" width="11" height="7.5" fill="#d9d9d9"/><path d="M0.5 2.5 6 7l5.5-4.5" fill="none" stroke="#161616" stroke-width="0.9"/></svg>
          <span>info@torvane.co.nz</span>
        </li>
      </ul>
    </div>
    <div class="card__stripe"></div>
  </section>

  <section class="card card--back" aria-label="Business card back">
    <div class="brand">
      <div class="brand__disc"></div>
      <p class="brand__name">Torvane Aviation Limited</p>
    </div>
  </section>

  <section class="lockup brand" aria-label="Company name lockup">
    <div class="brand__disc"></div>
    <p class="brand__name">Torvane Aviation Limited</p>
  </section>

</main>
</body>
</html>
```